TARVEL infographic (architecture design and basic content)

We would like an infographic that will include the content found in the attached pptx file and in the attached image. On the top of the infographic we would like the content of the powerpoint presentation and in the bottom we would like a redesign of the attached figure. The figure should have the color patterns of the project (see logo). It is important to have a nice redesign of the attached architecture (figure).

Target Market(s)

Policy Makers

Font styles to use
Sans Serif

Colors
33b8a4

Requirements
Must have
• The project must have the following scale:
• - 16:18 The content of the ppt should be placed on top (16:9) and the architecture (figure) should be placed at the bottom (16:9).
Nice to have
• I also attach the project's brochure which was designed a couple of months ago. This is just to showcase the colors etc. that we would like.

```html
<!DOCTYPE html>
<html lang="en">
<head>
<meta charset="utf-8">
<title>TARVEL – Universal Cybersecurity Toolkit for the Healthcare Industry</title>
<link href="https://fonts.googleapis.com/css2?family=Roboto:wght@300;400;500;700&display=swap" rel="stylesheet">
<style>
:root{
  --teal:#00a79d;
  --teal-text:#17a394;
  --ink:#3d3d3d;
  --ink-soft:#555;
  --navy:#2f3578;
  --panel-left:#efefef;
  --panel-right:#f4f5f5;
  --arch-bg:#c8d9d6;
  --env-bg:#f6f8f8;
  --sandbox-bg:#dde6ef;
  --decision:#acdcca;
  --auto:#aac4de;
  --privacy:#97afc8;
  --integration:#b8cde3;
  --kb:#5db6a9;
  --sim:#8fb4ae;
  --arrow:#4f8e96;
  --funder:#0d3a9a;
}
*{box-sizing:border-box;margin:0;padding:0}
html,body{width:1067px;height:1200px;overflow:hidden;background:#fff}
body{font-family:"Roboto",sans-serif;color:var(--ink);position:relative}
.abs{position:absolute}

/* header */
.brand{left:0;top:0;width:350px;height:146px;background:#fff;display:flex;align-items:center;padding-left:34px;gap:14px}
.brand-dot{width:76px;height:76px;border-radius:50%;border:7px solid var(--teal)}
.brand-name{font-size:50px;font-weight:300;color:var(--teal);letter-spacing:2px}
.title-band{left:350px;top:0;width:717px;height:146px;background:var(--teal);color:#fff;padding:48px 0 0 33px;font-size:34px;font-weight:700;line-height:42px;letter-spacing:.3px}

/* key facts */
.facts{left:0;top:146px;width:350px;height:544px;background:var(--panel-left)}
.facts-accent{left:0;top:148px;width:9px;height:60px;background:var(--teal)}
.facts-title{left:38px;top:160px;font-size:30px;font-weight:700;color:var(--teal)}
.fact{left:33px;font-size:21px;font-weight:300;color:var(--ink)}
.fact b{position:absolute;left:173px;font-weight:500;white-space:nowrap}
.link{left:52px;width:255px;height:38px;display:flex;align-items:center;gap:12px;font-size:20px;color:var(--navy)}
.link-ico{width:21px;height:21px;border-radius:50%;border:1.5px solid var(--teal);color:var(--teal);font-size:10px;font-weight:700;display:flex;align-items:center;justify-content:center}
.link-rule{left:48px;width:259px;height:1px;background:#bbb}
.partners{left:48px;top:481px;width:257px;height:120px;background:#fff;display:grid;grid-template-columns:repeat(5,1fr);gap:8px 8px;padding:14px 18px;align-content:center}
.partners span{height:17px;background:#d6d9dc;border-radius:3px}
.partners span.c{border-radius:50%;width:17px;justify-self:center}
.funder-flag{left:32px;top:616px;width:91px;height:61px;background:var(--funder)}
.funder-note{left:134px;top:615px;width:205px;font-size:10px;line-height:14px;color:#444}

/* goals */
.right{left:350px;top:146px;width:717px;height:544px;background:var(--panel-right)}
.h2{font-size:31px;font-weight:700;color:var(--ink-soft)}
.goals-text{left:444px;top:227px;width:580px;font-size:17px;line-height:26px;color:#444}
.goals-text b{font-weight:500}
.obj-list{left:455px;top:383px;list-style:none}
.obj-list li{display:flex;align-items:center;gap:12px;height:30.2px;font-size:17px;color:#444;letter-spacing:.3px}
.chev{width:13px;height:13px;border-radius:50%;border:1.5px solid var(--teal);flex:none;position:relative}
.chev::after{content:"";position:absolute;left:2.5px;top:3px;width:3px;height:3px;border-right:1.5px solid var(--teal);border-top:1.5px solid var(--teal);transform:rotate(45deg)}
.obj-rule{left:393px;top:556px;width:620px;height:1px;background:var(--teal)}
.pilots-ring{left:419px;top:576px;width:48px;height:48px;border-radius:50%;border:5px solid var(--teal)}
.pilots-label{left:401px;top:630px;font-size:30px;font-weight:700;color:var(--ink-soft)}
.pilots-rule{left:528px;top:580px;width:1px;height:98px;background:var(--teal)}
.country{display:flex;align-items:center;gap:9px;font-size:19px;font-weight:500;color:var(--teal-text)}
.flag{width:28px;height:28px;border-radius:50%}
.site{font-size:13.5px;line-height:20px;color:#444}

/* architecture */
.arch{left:0;top:690px;width:1067px;height:510px;background:var(--arch-bg)}
.arch-title{left:0;width:1170px;top:710px;text-align:center;font-size:16px;font-weight:500;letter-spacing:.6px;color:#243033}
.it-frame{left:248px;top:737px;width:785px;height:62px;border:1.5px solid #fff;border-radius:3px}
.box{position:absolute;background:#fff;display:flex;align-items:center;justify-content:center;text-align:center;font-size:12.5px;line-height:13.5px;color:#333;border-radius:2px}
.it{top:745px;width:97px;height:45px;font-size:13px;line-height:14px;box-shadow:0 1px 2px rgba(0,0,0,.08)}
.flow-note{font-size:10.5px;letter-spacing:.6px;color:#444;text-align:center;line-height:13px}
.env{left:241px;top:839px;width:800px;height:345px;background:var(--env-bg);border:1px dashed #8aa}
.sandbox-zone{left:892px;top:840px;width:148px;height:343px;background:var(--sandbox-bg)}
.env-title{left:241px;width:688px;top:850px;text-align:center;font-size:15px;font-weight:500;letter-spacing:.6px;color:var(--teal-text)}
.decision{left:263px;top:873px;width:129px;height:231px;background:var(--decision)}
.decision-label{left:263px;width:129px;top:1057px;text-align:center;font-size:12.5px;font-weight:500;line-height:13px;color:#2c5a52}
.auto{left:409px;top:873px;width:461px;height:195px;background:var(--auto)}
.privacy{left:747px;top:873px;width:123px;height:132px;background:var(--privacy)}
.auto-title{left:409px;width:338px;top:880px;text-align:center;font-size:13.5px;font-weight:500;letter-spacing:.5px;color:#233f72}
.privacy-title{left:747px;width:123px;top:881px;text-align:center;font-size:12px;color:#233040}
.ac{width:97px;height:44px}
.kb{left:593px;top:1076px;width:97px;height:44px;background:var(--kb);color:#fff;font-size:13px;border-radius:0}
.integration{left:264px;top:1128px;width:753px;height:47px;background:var(--integration);text-align:center;padding-top:6px;font-size:13px;color:#222;line-height:18px}
.integration b{font-weight:500}
.dv-title{left:892px;width:148px;top:864px;text-align:center;font-size:12.5px;line-height:13px;color:#333}
.sim{background:var(--sim);color:#fff;width:97px;height:44px;font-size:11.5px;line-height:12.5px}
.sandbox-frame{left:904px;top:964px;width:123px;height:80px;border:1px dashed #4ab0a3}
.sandbox-label{left:904px;width:123px;top:1024px;text-align:center;font-size:11.5px;color:#333}
.sandbox-name{left:892px;width:148px;top:1062px;text-align:center;font-size:13.5px;font-weight:500;line-height:14px;color:var(--teal-text)}
.ext{width:70px;font-size:12.5px;line-height:13.5px}
.actor{text-align:center;font-size:11.5px;line-height:14px;color:#222}
.actor-ring{width:42px;height:42px;border-radius:50%;border:4px solid var(--teal)}
.actor-gear{width:30px;height:30px;border-radius:50%;border:7px solid #333}
svg.wires{position:absolute;left:0;top:0;pointer-events:none}
</style>
</head>
<body>

<!-- header -->
<div class="abs brand"><div class="brand-dot"></div><div class="brand-name">TARVEL</div></div>
<div class="abs title-band">A UNIVERSAL CYBERSECURITY TOOLKIT<br>FOR THE HEALTHCARE INDUSTRY</div>

<!-- key facts -->
<div class="abs facts"></div>
<div class="abs facts-accent"></div>
<div class="abs facts-title">KEY FACTS</div>
<div class="abs fact" style="top:212px">Starting Date:<b>1/1/2019</b></div>
<div class="abs fact" style="top:246px">Project Duration:<b>36 months</b></div>
<div class="abs fact" style="top:280px">EC Funding:<b>€ 4,999,435</b></div>
<div class="abs fact" style="top:314px">17 partners / 9 EU countries</div>

<div class="abs link" style="top:355px"><span class="link-ico">www</span>www.tarvel-project.eu</div>
<div class="abs link-rule" style="top:394px"></div>
<div class="abs link" style="top:394px"><span class="link-ico">@</span>ProjectTarvel</div>
<div class="abs link-rule" style="top:430px"></div>
<div class="abs link" style="top:433px"><span class="link-ico">in</span>tarvel-project</div>

<div class="abs partners" role="img" aria-label="Partner organisation badges">
  <span class="c"></span><span></span><span></span><span></span><span></span>
  <span></span><span></span><span class="c"></span><span></span><span class="c"></span>
  <span></span><span></span><span></span><span></span><span></span>
  <span></span><span></span><span></span><span></span><span class="c"></span>
</div>
<div class="abs funder-flag" role="img" aria-label="Funding body badge"></div>
<div class="abs funder-note">TARVEL Project has received funding from the Northern Research Council’s Frontier 2030 research and innovation programme under grant agreement No 800417.</div>

<!-- goals & objectives -->
<div class="abs right" role="img" aria-label="Faint world map background"></div>

<svg class="abs" style="left:389px;top:176px" width="40" height="44" viewBox="0 0 40 44">
  <path d="M20 2 L37 8 V20 C37 31 29 38 20 42 C11 38 3 31 3 20 V8 Z" fill="none" stroke="var(--teal)" stroke-width="3"/>
  <circle cx="20" cy="21" r="11" fill="var(--teal)"/>
  <rect x="15" y="20" width="10" height="8" rx="1" fill="#fff"/>
  <path d="M17 20 v-3 a3 3 0 0 1 6 0 v3" fill="none" stroke="#fff" stroke-width="1.8"/>
</svg>
<div class="abs h2" style="left:444px;top:178px">GOALS</div>
<div class="abs goals-text">TARVEL aims to introduce a <b>health tailored Universal Cybersecurity Toolkit</b>, thus enhancing the <b>cyber protection of the Health and care IT Ecosystem</b> and ensuring patient data privacy and integrity.</div>

<svg class="abs" style="left:386px;top:332px" width="46" height="44" viewBox="0 0 46 44">
  <circle cx="20" cy="24" r="17" fill="none" stroke="var(--teal)" stroke-width="4"/>
  <circle cx="20" cy="24" r="9" fill="none" stroke="var(--teal)" stroke-width="4"/>
  <circle cx="20" cy="24" r="3" fill="var(--teal)"/>
  <path d="M20 24 L38 6" stroke="var(--teal)" stroke-width="3.5"/>
  <path d="M34 4 L42 2 L40 10 Z" fill="var(--teal)"/>
</svg>
<div class="abs h2" style="left:444px;top:334px">OBJECTIVES</div>
<ul class="abs obj-list">
  <li><span class="chev"></span>Cyber protection and data privacy and integrity</li>
  <li><span class="chev"></span>Proactive assessment and mitigation of Cybersecurity threats</li>
  <li><span class="chev"></span>Evaluation and verification of new Medical Devices &amp; Services</li>
  <li><span class="chev"></span>Provision of the TARVEL Certification</li>
  <li><span class="chev"></span>Near real-time vulnerability assessment of operating IT Ecosystems</li>
</ul>
<div class="abs obj-rule"></div>

<!-- pilots -->
<div class="abs pilots-ring"></div>
<div class="abs pilots-label">PILOTS</div>
<div class="abs pilots-rule"></div>

<div class="abs country" style="left:558px;top:575px"><span class="flag" style="background:#1d5fb5" role="img" aria-label="Flag of Greece"></span>GREECE</div>
<div class="abs site" style="left:559px;top:610px">University Hospital of<br>Meridia, the General<br>Hospital of Kostra</div>

<div class="abs country" style="left:733px;top:575px"><span class="flag" style="background:#d8242a" role="img" aria-label="Flag of Spain"></span>SPAIN</div>
<div class="abs site" style="left:734px;top:610px">The Hospital do<br>Vale Claro</div>

<div class="abs country" style="left:881px;top:575px"><span class="flag" style="background:#1c7a3a" role="img" aria-label="Flag of Portugal"></span>PORTUGAL</div>
<div class="abs site" style="left:882px;top:610px">the Aurelis Medical<br>Clinical</div>

<!-- architecture -->
<div class="abs arch"></div>
<div class="abs arch-title">HEALTHCARE IT OPERATIONAL ENVIRONMENT</div>
<div class="abs it-frame"></div>
<div class="box it" style="left:259px">Users</div>
<div class="box it" style="left:370px">Workstations</div>
<div class="box it" style="left:481px">BYOD</div>
<div class="box it" style="left:592px">Servers</div>
<div class="box it" style="left:703px">Network<br>Equipment</div>
<div class="box it" style="left:814px">Healthcare<br>Devices</div>
<div class="box it" style="left:925px">Software<br>Applications</div>
<div class="abs flow-note" style="left:330px;width:296px;top:807px">System Alerts, Machine and Process Monitoring,<br>User Access Monitoring</div>
<div class="abs flow-note" style="left:670px;width:300px;top:813px">Network Traffic, System Logs, Device Discovery</div>

<div class="abs env"></div>
<div class="abs sandbox-zone"></div>
<div class="abs env-title">TARVEL OPERATIONAL ENVIRONMENT</div>

<div class="abs decision"></div>
<div class="box ac" style="left:279px;top:898px">Decision<br>Support System</div>
<div class="box ac" style="left:279px;top:953px">Analytic<br>Engine</div>
<div class="box ac" style="left:279px;top:1005px">Interactive<br>Dashboard</div>
<div class="abs decision-label">Decision Support<br>and Interactive<br>Dashboard</div>

<div class="abs auto"></div>
<div class="abs privacy"></div>
<div class="abs auto-title">AUTOMATED CYBER SECURITY</div>
<div class="abs privacy-title">Privacy Tools</div>
<div class="box ac" style="left:424px;top:901px">Data Traffic<br>Monitoring</div>
<div class="box ac" style="left:531px;top:901px;font-size:10.5px;line-height:12.5px">Security<br>Information and<br>Event Management</div>
<div class="box ac" style="left:638px;top:901px">AI<br>Honeypot</div>
<div class="box ac" style="left:760px;top:901px">Homomorphic<br>Encryption</div>
<div class="box ac" style="left:424px;top:956px">Anomaly<br>Detection</div>
<div class="box ac" style="left:531px;top:956px;font-size:12px">Forensics Data<br>Collection Engine</div>
<div class="box ac" style="left:638px;top:956px;font-size:11px">Machine Learning<br>Intrusion Detection</div>
<div class="box ac" style="left:760px;top:956px">Anonymisation<br>and Privacy</div>
<div class="box ac" style="left:424px;top:1008px;font-size:12px">Security Protocol<br>Analysis</div>
<div class="box ac" style="left:531px;top:1008px;font-size:12px">Blockchain Based<br>Threat Registry</div>
<div class="box ac" style="left:638px;top:1008px;font-size:11.5px">Real-time Cyber<br>Risk Assessment</div>
<div class="box ac" style="left:760px;top:1008px;font-size:12px">Vulnerability<br>Assessment<br>as a Service</div>

<div class="box kb">Knowledge<br>Base</div>

<div class="abs integration"><b>Common Integration Platform</b><br>Authentication &nbsp;| &nbsp;Data Bus and Middleware &nbsp;| &nbsp;APIs &nbsp;| &nbsp;Big Data</div>

<div class="abs dv-title">Device Verification<br>and Certification</div>
<div class="box sim" style="left:917px;top:906px">Attack and<br>Behaviours<br>Simulators</div>
<div class="abs sandbox-frame"></div>
<div class="box sim" style="left:917px;top:974px">Automated<br>Cyber Security<br>Certification</div>
<div class="abs sandbox-label">SANDBOX</div>
<div class="abs sandbox-name">TARVEL<br>Sandboxed<br>Environment</div>

<!-- external actors -->
<div class="abs actor-ring" style="left:48px;top:873px"></div>
<div class="abs actor" style="left:38px;top:936px;width:60px">TARVEL<br>User</div>
<div class="box ext" style="left:132px;top:860px;height:70px"><span>⚙<br>Cyber<br>Security<br>Toolbox</span></div>
<div class="abs actor-gear" style="left:54px;top:1030px"></div>
<div class="abs actor" style="left:28px;top:1066px;width:80px">Third Party<br>Component</div>
<div class="box ext" style="left:132px;top:1023px;height:47px">Third<br>Party APIs</div>

<svg class="wires" width="1067" height="1200" viewBox="0 0 1067 1200">
  <defs>
    <marker id="tip" viewBox="0 0 10 10" refX="8" refY="5" markerWidth="4" markerHeight="4" orient="auto-start-reverse">
      <path d="M0 0 L10 5 L0 10 Z" fill="var(--arrow)"/>
    </marker>
  </defs>
  <g stroke="var(--arrow)" stroke-width="3" fill="none" marker-start="url(#tip)" marker-end="url(#tip)">
    <line x1="306" y1="802" x2="306" y2="835"/>
    <line x1="644" y1="802" x2="644" y2="835"/>
    <line x1="978" y1="802" x2="978" y2="835"/>
    <line x1="95" y1="891" x2="128" y2="891"/>
    <line x1="206" y1="891" x2="238" y2="891"/>
    <line x1="92" y1="951" x2="238" y2="951"/>
    <line x1="95" y1="1045" x2="128" y2="1045"/>
    <line x1="206" y1="1045" x2="238" y2="1045"/>
    <line x1="876" y1="1001" x2="910" y2="1001"/>
    <line x1="816" y1="1070" x2="816" y2="1115"/>
  </g>
  <g stroke="var(--arrow)" stroke-width="3" fill="none" marker-end="url(#tip)">
    <line x1="642" y1="1076" x2="642" y2="1057"/>
    <line x1="594" y1="1078" x2="581" y2="1065"/>
    <line x1="690" y1="1078" x2="704" y2="1064"/>
    <line x1="591" y1="1106" x2="560" y2="1106"/>
    <line x1="693" y1="1106" x2="724" y2="1106"/>
  </g>
</svg>

</body>
</html>
```